Need a new office flyer

I would like an 8.5 x 11" flyer made that can be emailed or printed out and handed to potential customers.  The flyer should include our existing logo and continuity of branding.   I am a commercial real estate broker and market myself to business with 5-50 employee's that are looking to buy or lease space to run their business from.  I focus my efforts on office & warehouse space. The flyer should have a banner "need a new location "
"LVW commercial real estate specializes in helping business and professionals buy/sell or lease  the best spaces for their business.  Take the stress & time out of finding the best location for your business and negotiating a great deal  LVW will do it for you and the best part our service is free to you. Working with LVW is easy as 1, 2, 3
1. Call, Text, Email us today and let us know what your looking to do.
2. LVW  will prepare a list of all the best available spaces that meet your specifications and set up tours of your favorites.
3. We will negotiate the best terms for your space. and help you with all the  details of getting your new space ready for you.
Don't forget the that our services are free to Buyers and Tenants so don't waste your companies time searching for locations, we already know where they are!
Contact us today!
Dale Pruitt
DRE 04871326
LVW Commercial Real Estate
530-417-2296
d.pruitt@lvwholdings.example

```html
<!DOCTYPE html>
<html lang="en">
<head>
<meta charset="utf-8">
<title>LVW Commercial Real Estate – Need a New Location</title>
<link rel="stylesheet" href="https://fonts.googleapis.com/css2?family=Titillium+Web:wght@300;400;600;700&display=swap">
<style>
  :root {
    --brand-blue: #2a6da3;
    --brand-blue-deep: #215a8a;
    --ink: #2b2b2b;
    --grey: #9a9a9a;
    --pale: #f1f2f4;
    --white: #ffffff;
    --backdrop: #d8d9db;
  }
  * { margin: 0; padding: 0; box-sizing: border-box; }
  html, body { width: 1200px; height: 1128px; overflow: hidden; }
  body {
    background: var(--backdrop);
    font-family: "Titillium Web", Arial, sans-serif;
    color: var(--ink);
  }
  .flyer {
    position: absolute; left: 160px; top: 0;
    width: 880px; height: 1128px;
    background: linear-gradient(180deg, var(--white) 55%, var(--pale) 75%, var(--white) 92%);
    overflow: hidden;
  }
  .hero-band { position: absolute; left: 0; top: 0; }

  .brand { position: absolute; left: 46px; top: 44px; display: flex; align-items: center; gap: 12px; }
  .brand-dot {
    width: 104px; height: 104px; border-radius: 50%;
    border: 5px solid var(--brand-blue);
    flex: none;
  }
  .brand-name { color: var(--brand-blue); font-weight: 700; line-height: 1; }
  .brand-name .big { display: block; font-size: 76px; letter-spacing: 2px; line-height: 70px; }
  .brand-name .small { display: block; font-size: 12px; letter-spacing: 5px; margin-top: 6px; }

  .map-art {
    position: absolute; left: 470px; top: 46px; width: 410px; height: 304px;
    background: linear-gradient(160deg, #e9e6df 0%, #cfe4b8 40%, #e8e4da 70%, #d7e3ee 100%);
    border-radius: 4px;
  }

  .headline {
    position: absolute; left: 44px; top: 178px;
    color: var(--white); font-weight: 700;
    font-size: 118px; line-height: 90px; letter-spacing: -1px;
    text-transform: uppercase;
  }

  .intro {
    position: absolute; left: 96px; top: 492px; width: 744px;
    color: var(--white); font-size: 17px; line-height: 20.6px;
  }
  .intro-arrow { position: absolute; left: 55px; top: 494px; }

  .steps { position: absolute; left: 48px; top: 610px; width: 790px; height: 250px; }
  .step {
    position: absolute; top: 47px; width: 249px; height: 184px;
    border: 2px solid var(--brand-blue); border-radius: 12px;
    background: var(--white);
    box-shadow: 0 14px 12px -12px rgba(0,0,0,0.25);
    text-align: center; font-size: 17.5px; line-height: 22px;
    padding: 62px 26px 0;
  }
  .step-icon {
    position: absolute; top: -48px; left: 50%; margin-left: -48px;
    width: 96px; height: 96px; border-radius: 50%;
    background: var(--brand-blue);
    display: flex; align-items: center; justify-content: center;
  }
  .step-1 { left: 0; }
  .step-2 { left: 267px; }
  .step-3 { left: 534px; }

  .reminder {
    position: absolute; left: 0; width: 880px; top: 876px;
    text-align: center; font-size: 21px; line-height: 28px; font-weight: 300;
  }
  .reminder strong { color: var(--brand-blue); font-weight: 600; }
  .tagline {
    position: absolute; left: 0; width: 880px; top: 934px;
    text-align: center; font-size: 38px; font-weight: 700; line-height: 48px;
    color: var(--ink);
  }

  .contact-band {
    position: absolute; left: 0; top: 996px; width: 760px; height: 45px;
    background: var(--brand-blue);
    display: flex; align-items: center; padding-left: 32px;
  }
  .contact-band span { color: var(--white); font-weight: 700; font-size: 29px; line-height: 1; }
  .contact-band i { display: block; height: 2px; width: 185px; background: var(--white); margin-left: 14px; }

  .corner-mark {
    position: absolute; left: 734px; top: 966px;
    width: 156px; height: 156px; border-radius: 50%;
    background: var(--white); border: 6px solid var(--brand-blue);
    display: flex; align-items: center; justify-content: center;
    color: var(--brand-blue); font-weight: 700; font-size: 44px;
  }

  .agent { position: absolute; left: 31px; top: 1052px; line-height: 1; }
  .agent-name { color: var(--brand-blue); font-weight: 700; font-size: 30px; }
  .agent-licence { font-weight: 700; font-size: 19px; margin-top: 4px; }

  .phone-icon { position: absolute; left: 216px; top: 1058px; }
  .office { position: absolute; left: 256px; top: 1055px; line-height: 1; }
  .office-name { font-size: 15px; font-weight: 400; }
  .office-phone { color: var(--brand-blue); font-weight: 700; font-size: 35px; margin-top: 3px; }
  .divider { position: absolute; left: 486px; top: 1060px; width: 1px; height: 46px; background: var(--ink); }
  .globe-icon { position: absolute; left: 506px; top: 1070px; }
  .web { position: absolute; left: 536px; top: 1060px; font-size: 14px; line-height: 22px; font-weight: 600; }
</style>
</head>
<body>
<main class="flyer">
  <svg class="hero-band" width="880" height="590" viewBox="0 0 880 590" aria-hidden="true">
    <defs>
      <linearGradient id="heroBlue" x1="0" y1="0" x2="0" y2="1">
        <stop offset="0" stop-color="#2b70a8"/>
        <stop offset="1" stop-color="#235e90"/>
      </linearGradient>
    </defs>
    <polygon points="564,0 880,0 880,590 0,590 0,165 471,165" fill="url(#heroBlue)"/>
  </svg>

  <div class="brand">
    <div class="brand-dot"></div>
    <div class="brand-name"><span class="big">LVW</span><span class="small">COMMERCIAL REAL ESTATE</span></div>
  </div>

  <div class="map-art" role="img" aria-label="Illustration of a hand placing a red location pin on a folded city street map"></div>

  <h1 class="headline">Need<br>A New<br>Location</h1>

  <svg class="intro-arrow" width="26" height="76" viewBox="0 0 26 76" aria-hidden="true">
    <polygon points="0,0 26,38 0,76" fill="#d5d9dd"/>
  </svg>
  <p class="intro">LVW commercial real estate specializes in helping business and professionals buy/sell or lease the best spaces for their business. Take the stress &amp; time out of finding the best location for your business and negotiating a great deal LVW will do it for you and the best part our service is free to you. Working with LVW is easy as 1, 2, 3</p>

  <section class="steps">
    <div class="step step-1">
      <div class="step-icon">
        <svg width="70" height="70" viewBox="0 0 70 70" aria-hidden="true">
          <circle cx="35" cy="35" r="31" fill="none" stroke="#fff" stroke-width="3"/>
          <path d="M24 20c2-2 5-2 6 1l3 6c1 2 0 4-2 5l-2 2c2 5 6 9 11 11l2-2c1-2 3-3 5-2l6 3c3 1 3 4 1 6l-3 3c-3 3-10 2-18-6s-9-15-6-18z" fill="none" stroke="#fff" stroke-width="3" stroke-linejoin="round"/>
        </svg>
      </div>
      Call, Text, Email us today and let us know what your looking to do
    </div>
    <div class="step step-2">
      <div class="step-icon">
        <svg width="70" height="70" viewBox="0 0 70 70" aria-hidden="true">
          <rect x="14" y="10" width="34" height="50" rx="3" fill="none" stroke="#fff" stroke-width="3"/>
          <g stroke="#fff" stroke-width="2.5" fill="none">
            <path d="M19 20l3 3 4-5M19 30l3 3 4-5M19 40l3 3 4-5M19 50l3 3 4-5"/>
            <path d="M30 21h13M30 31h13M30 41h13M30 51h13"/>
            <rect x="53" y="16" width="5" height="38" rx="1"/>
            <path d="M53 16l2.5-6 2.5 6"/>
          </g>
        </svg>
      </div>
      LVW will prepare a list of all the best available spaces that meet your specifications and set up tours of your favorites.
    </div>
    <div class="step step-3">
      <div class="step-icon">
        <svg width="72" height="72" viewBox="0 0 72 72" aria-hidden="true">
          <g fill="none" stroke="#fff" stroke-width="3" stroke-linejoin="round" stroke-linecap="round">
            <path d="M6 22l10-8 8 12-10 8z"/>
            <path d="M66 22l-10-8-8 12 10 8z"/>
            <path d="M24 24l10-4c3-1 6 0 8 2l10 10"/>
            <path d="M48 26l-12 2-6 6c-2 2 1 5 3 3l6-4"/>
            <path d="M14 34l18 18c2 2 5-1 3-3M22 42l12 12c2 2 5-1 3-3M28 38l12 12c2 2 5-1 3-3M52 32l-9 14"/>
          </g>
        </svg>
      </div>
      We will negotiate the best terms for your space. and help you with all the details of getting your new space ready for you.
    </div>
  </section>

  <p class="reminder">Don't forget the that <strong>our services are free to Buyers and Tenants so<br>don't waste your companies time searching for locations</strong></p>
  <p class="tagline">WE ALREADY KNOW WHERE THEY ARE!</p>

  <div class="contact-band"><span>FOR MORE DETAILS, CONTACT US TODAY!</span><i></i></div>
  <div class="corner-mark">LVW</div>

  <div class="agent">
    <div class="agent-name">DALE PRUITT</div>
    <div class="agent-licence">DRE 04871326</div>
  </div>

  <svg class="phone-icon" width="26" height="46" viewBox="0 0 26 46" aria-hidden="true">
    <rect x="1.5" y="1.5" width="23" height="43" rx="4" fill="none" stroke="#555" stroke-width="2.5"/>
    <line x1="9" y1="39" x2="17" y2="39" stroke="#555" stroke-width="2"/>
  </svg>
  <div class="office">
    <div class="office-name">LVW COMMERCIAL REAL ESTATE</div>
    <div class="office-phone">530-417-2296</div>
  </div>
  <div class="divider"></div>

  <svg class="globe-icon" width="26" height="26" viewBox="0 0 26 26" aria-hidden="true">
    <g fill="none" stroke="#555" stroke-width="1.6">
      <circle cx="13" cy="13" r="11.5"/>
      <ellipse cx="13" cy="13" rx="5" ry="11.5"/>
      <path d="M1.5 13h23M3.5 7h19M3.5 19h19"/>
    </g>
  </svg>
  <div class="web">d.pruitt@lvwholdings.example<br>www.lvwholdings.example</div>
</main>
</body>
</html>
```